Candle Box & Belly Band Design

Design Candle Box for Soy Candles along with a belly band design that can be used on off the shelf coloured boxes. It is for a premium brand of candle - so i want the packaging to reflect this. I have included must haves below.

The candle boxes will be a few different sizes, but for the purpose of the design it would be something like a cube 12 x 12 x 12 cms

The belly band for standard boxes to be something like 5cm wide on a 12 x 12 x 12cms cube box that goes all the way around the top to the bottom - holding the lid on and providing all the relevant information. Example of box with belly band uploaded

Our company Name : Fern & Isla - our logo is uploaded

Target Market(s)

Premium Candle Buyers

Colors

Designer to choose colors to be used in the design.

Requirements
Must have
• Must have our logo - our logo can be in any colour
• Must state:
• Soy Candle, Hand Poured, Made in Melbourne,
• A space for the fragrance, size and burn time.
• For this project use Lime, Coconut & Elderfllower, 300grams, 50 Hour burn Time

```html
<!DOCTYPE html>
<html lang="en">
<head>
<meta charset="utf-8">
<title>Fern &amp; Isla Soy Candle Belly Band</title>
<link rel="stylesheet" href="https://fonts.googleapis.com/css2?family=Great+Vibes&family=Quicksand:wght@400;500;600&display=swap">
<style>
  :root {
    --page-bg: #e9eaec;
    --band-black: #050505;
    --gold: #c8a84b;
    --gold-light: #e2c872;
    --gold-rule: #8f7634;
  }
  * { margin: 0; padding: 0; box-sizing: border-box; }
  html, body {
    width: 1200px;
    height: 923px;
    overflow: hidden;
    background: var(--page-bg);
  }
  .canvas {
    position: relative;
    width: 1200px;
    height: 923px;
    background: radial-gradient(ellipse at center, #f6f6f7 0%, var(--page-bg) 75%);
  }
  .belly-band {
    position: absolute;
    left: 435px;
    top: 61px;
    width: 330px;
    height: 800px;
    background: var(--band-black);
    box-shadow: 0 6px 22px rgba(0, 0, 0, 0.18);
    text-align: center;
    color: var(--gold);
    font-family: "Quicksand", sans-serif;
  }
  .gold-rule {
    position: absolute;
    top: 0;
    bottom: 0;
    width: 3px;
    background: linear-gradient(180deg, var(--gold-rule), var(--gold-light) 50%, var(--gold-rule));
  }
  .gold-rule--left { left: 18px; }
  .gold-rule--right { right: 18px; }

  .brand {
    position: absolute;
    top: 62px;
    left: 0;
    right: 0;
    display: flex;
    flex-direction: column;
    align-items: center;
    gap: 14px;
  }
  .brand-dot {
    width: 58px;
    height: 58px;
    border-radius: 50%;
    background: var(--gold);
  }
  .brand-name {
    font-size: 19px;
    font-weight: 500;
    color: var(--gold);
    letter-spacing: 0.3px;
  }

  .product-title {
    position: absolute;
    top: 225px;
    left: 0;
    right: 0;
    font-family: "Great Vibes", cursive;
    font-weight: 400;
    color: var(--gold-light);
    font-size: 100px;
    line-height: 88px;
  }
  .product-title span { display: block; }
  .product-title .title-soy { padding-left: 10px; }

  .fragrance {
    position: absolute;
    top: 445px;
    left: 0;
    right: 0;
    font-size: 28px;
    font-weight: 400;
    line-height: 37px;
    color: var(--gold);
  }

  .details {
    position: absolute;
    top: 595px;
    left: 0;
    right: 0;
  }
  .hand-poured {
    display: flex;
    align-items: center;
    justify-content: center;
    gap: 8px;
  }
  .flame-icon { width: 22px; height: 34px; }
  .hand-poured-text { text-align: left; }
  .hand-poured-title {
    font-size: 22px;
    font-weight: 400;
    line-height: 24px;
  }
  .burn-time {
    font-size: 17px;
    font-weight: 400;
    line-height: 20px;
  }
  .weight {
    margin-top: 18px;
    font-size: 24px;
    font-weight: 400;
  }
  .origin {
    margin-top: 14px;
    display: flex;
    align-items: center;
    justify-content: center;
    gap: 6px;
    font-size: 20px;
    font-weight: 600;
    color: var(--gold-light);
  }
  .origin-mark {
    width: 28px;
    height: 15px;
    background: var(--gold-rule);
  }
</style>
</head>
<body>
<main class="canvas">
  <section class="belly-band" aria-label="Soy candle belly band">
    <div class="gold-rule gold-rule--left"></div>
    <div class="gold-rule gold-rule--right"></div>

    <header class="brand">
      <div class="brand-dot"></div>
      <p class="brand-name">Fern &amp; Isla</p>
    </header>

    <h1 class="product-title">
      <span class="title-soy">Soy</span>
      <span class="title-candle">Candle</span>
    </h1>

    <p class="fragrance">Lime, Coconut<br>&amp; Elderflower</p>

    <div class="details">
      <div class="hand-poured">
        <svg class="flame-icon" viewBox="0 0 22 34" aria-hidden="true">
          <path d="M11 1 C14 8 20 12 20 21 C20 28 16 33 11 33 C6 33 2 28 2 22 C2 16 6 13 7 8 C9 12 8 16 10 18 C12 13 9 7 11 1 Z" fill="#c8a84b"/>
          <path d="M11 20 C13 23 15 25 14 29 C13 31 9 31 8 29 C7 26 10 24 11 20 Z" fill="#050505"/>
        </svg>
        <div class="hand-poured-text">
          <p class="hand-poured-title">Hand Poured</p>
          <p class="burn-time">50 Hour burn Time</p>
        </div>
      </div>
      <p class="weight">300 gr</p>
      <p class="origin"><span class="origin-mark"></span>Made in Melbourne</p>
    </div>
  </section>
</main>
</body>
</html>
```